Realtor Second mailing to my Farm Area

Doing a second mailing to my farm area. Will be sending out a postcard or some mailing every month or every other month. Going to have my companys LOGO cover a big portion of the postcard. Then my picture. Then a picture of a sold listing or area of the downtown. Also something like "My 20 Years Real Estate Experience available to you should you be thinking of Buying or Selling a home"

```html
<!DOCTYPE html>
<html lang="en">
<head>
<meta charset="utf-8">
<title>Realtor Farm Area Postcard</title>
<link href="https://fonts.googleapis.com/css2?family=Open+Sans:wght@400;600;700&family=Great+Vibes&display=swap" rel="stylesheet">
<style>
  :root {
    --brand-red: #c8174a;
    --brand-red-dark: #a3123b;
    --brand-pink: #e0245f;
    --paper: #ffffff;
    --stage: #ecebe8;
    --ink-light: #ffffff;
    --line-grey: #c9c9c9;
    --sky-pink: #c98a9a;
    --lawn: #5f8f3a;
  }
  * { box-sizing: border-box; margin: 0; padding: 0; }
  html, body { width: 1200px; height: 729px; overflow: hidden; }
  body {
    background: var(--stage);
    font-family: "Open Sans", Arial, sans-serif;
    position: relative;
  }
  .postcard {
    position: absolute;
    top: 175px;
    width: 570px;
    height: 380px;
    background: var(--paper);
    overflow: hidden;
  }
  .postcard--back { left: 20px; }
  .postcard--front { left: 610px; }

  /* ---------- back side ---------- */
  .back-brand-panel {
    position: absolute; left: 0; top: 0; width: 390px; height: 232px;
    background: linear-gradient(180deg, var(--brand-red) 0%, var(--brand-red-dark) 100%);
  }
  .brand-name {
    color: var(--ink-light);
    font-family: "Open Sans", Arial, sans-serif;
    font-weight: 600;
    text-align: right;
    line-height: 1.15;
  }
  .back-brand-panel .brand-name {
    position: absolute; left: 10px; top: 55px; width: 152px; font-size: 17px;
  }
  .back-divider {
    position: absolute; left: 170px; top: 40px; width: 1px; height: 95px;
    background: rgba(255,255,255,0.7);
  }
  .back-contacts {
    position: absolute; left: 178px; top: 42px; list-style: none;
    color: var(--ink-light); font-size: 9.5px; font-weight: 600; line-height: 1.3;
  }
  .back-contacts li { display: flex; align-items: flex-start; gap: 6px; margin-bottom: 8px; }
  .icon-dot {
    flex: none; width: 13px; height: 13px; border-radius: 50%;
    background: var(--ink-light);
    display: inline-flex; align-items: center; justify-content: center;
  }
  .icon-dot svg { width: 8px; height: 8px; fill: var(--brand-red); }

  .back-photo-strip {
    position: absolute; left: 0; top: 232px; width: 390px; height: 92px; background: var(--paper);
  }
  .agent-portrait {
    position: absolute;
    background: linear-gradient(180deg, #d9c8a8 0%, #c9b08a 45%, #2a2a2a 70%, #1b1b1b 100%);
  }
  .back-portrait { left: 2px; top: 198px; width: 88px; height: 142px; }
  .listing-photo {
    position: absolute; top: 244px; width: 94px; height: 70px;
    background: linear-gradient(180deg, #9fc3e6 0%, #cfd6c9 45%, #6e9a4a 75%, #4f7c33 100%);
  }
  .listing-photo--one { left: 93px; }
  .listing-photo--two { left: 192px; background: linear-gradient(180deg, #dfe3e4 0%, #e8e8e4 40%, #5c7d3f 75%, #3f5f2a 100%); }
  .listing-photo--three { left: 291px; width: 96px; background: linear-gradient(180deg, #7e9d72 0%, #a58a6c 45%, #6b9b45 80%, #4c7a30 100%); }
  .back-footer-bar {
    position: absolute; left: 90px; top: 324px; width: 300px; height: 16px;
    background: var(--brand-red-dark);
  }
  .stamp-box {
    position: absolute; left: 478px; top: 8px; width: 74px; height: 84px;
    border: 1px solid var(--line-grey);
  }
  .address-lines { position: absolute; left: 410px; top: 220px; width: 145px; }
  .address-lines span {
    display: block; height: 1px; background: var(--line-grey); margin-bottom: 27px;
  }

  /* ---------- front side ---------- */
  .front-scene {
    position: absolute; inset: 0;
    background: linear-gradient(180deg, #b9c6d4 0%, #dfe4e8 40%, #9a9a92 52%, #7d8a6f 62%, var(--lawn) 78%, #4d7a2f 100%);
  }
  .front-sky {
    position: absolute; left: 0; top: 0; width: 100%; height: 118px;
    background: linear-gradient(180deg, #b77f91 0%, var(--sky-pink) 60%, #d9a9b4 100%);
  }
  .front-brand-box {
    position: absolute; left: 388px; top: 16px; width: 178px; height: 110px;
    background: var(--brand-red);
    display: flex; align-items: center; justify-content: center;
  }
  .front-brand-box .brand-name { font-size: 20px; text-align: center; }
  .front-portrait { left: 0; top: 40px; width: 222px; height: 300px; }
  .front-message {
    position: absolute; left: 246px; top: 172px; color: var(--ink-light);
  }
  .message-lead { font-size: 19px; font-weight: 700; line-height: 1.1; }
  .message-script {
    font-family: "Great Vibes", cursive; color: var(--brand-pink);
    font-size: 30px; line-height: 0.95; white-space: nowrap;
  }
  .message-body { font-size: 14px; line-height: 1.25; }
  .front-footer {
    position: absolute; left: 0; top: 325px; width: 100%; height: 40px;
    background: linear-gradient(90deg, #e6407a 0%, var(--brand-red) 55%, var(--brand-red-dark) 100%);
    display: flex; align-items: center;
  }
  .front-footer-base {
    position: absolute; left: 0; top: 365px; width: 100%; height: 15px; background: #e9dfe2;
  }
  .agent-signature { position: absolute; left: 12px; top: -6px; color: var(--ink-light); }
  .agent-name { font-family: "Great Vibes", cursive; font-size: 30px; line-height: 1; }
  .agent-title {
    font-family: "Great Vibes", cursive; font-size: 18px; position: absolute; left: 118px; top: 26px;
  }
  .front-phones {
    position: absolute; right: 10px; top: 12px; list-style: none; display: flex; gap: 12px;
    color: var(--ink-light); font-size: 12px; font-weight: 700;
  }
  .front-phones li { display: flex; align-items: center; gap: 4px; }
</style>
</head>
<body>

<section class="postcard postcard--back" aria-label="Postcard back">
  <div class="back-brand-panel">
    <div class="brand-name">Marlow Ashby<br>Associates</div>
    <div class="back-divider"></div>
    <ul class="back-contacts">
      <li><span class="icon-dot"><svg viewBox="0 0 10 10"><path d="M5 1 L9 5 H8 V9 H6 V6.5 H4 V9 H2 V5 H1 Z"/></svg></span><span>Marlow Ashby + Associates, Inc.<br>418 N. Lakeview Ave., Cedar Glen, FL 32701</span></li>
      <li><span class="icon-dot"><svg viewBox="0 0 10 10"><path d="M2.2 1 L4 1.2 L4.6 3.2 L3.6 4 Q4.4 5.8 6 6.4 L6.8 5.4 L8.8 6 L9 7.8 Q8 9 6.8 8.8 Q2.4 7.8 1.2 3.2 Q1 2 2.2 1 Z"/></svg></span><span>555-210-4400 ext. 220</span></li>
      <li><span class="icon-dot"><svg viewBox="0 0 10 10"><rect x="1" y="3" width="8" height="5" rx="1"/><rect x="3" y="1.5" width="4" height="2"/></svg></span><span>555-210-4471</span></li>
      <li><span class="icon-dot"><svg viewBox="0 0 10 10"><rect x="3" y="1" width="4" height="8" rx="0.8"/></svg></span><span>555-318-2260</span></li>
    </ul>
  </div>
  <div class="back-photo-strip"></div>
  <div class="listing-photo listing-photo--one" role="img" aria-label="Photo of a single-storey home with lawn"></div>
  <div class="listing-photo listing-photo--two" role="img" aria-label="Photo of a white two-storey home with garden"></div>
  <div class="listing-photo listing-photo--three" role="img" aria-label="Photo of a home behind trees and a lawn"></div>
  <div class="back-footer-bar"></div>
  <div class="agent-portrait back-portrait" role="img" aria-label="Portrait photo of the realtor"></div>
  <div class="stamp-box"></div>
  <div class="address-lines"><span></span><span></span><span></span><span></span></div>
</section>

<section class="postcard postcard--front" aria-label="Postcard front">
  <div class="front-scene" role="img" aria-label="Photo of a sold single-storey home with a green lawn under a cloudy sky"></div>
  <div class="front-sky"></div>
  <div class="front-brand-box"><div class="brand-name">Marlow Ashby<br>Associates</div></div>
  <div class="agent-portrait front-portrait" role="img" aria-label="Portrait photo of the realtor"></div>
  <div class="front-message">
    <p class="message-lead">My 20 Years</p>
    <p class="message-script">Real Estate Experience</p>
    <p class="message-body">available to you should you be thinking<br>of Buying or Selling a home</p>
  </div>
  <div class="front-footer">
    <div class="agent-signature">
      <span class="agent-name">Dana Whitfield</span>
      <span class="agent-title">Realtor</span>
    </div>
    <ul class="front-phones">
      <li><span class="icon-dot"><svg viewBox="0 0 10 10"><path d="M2.2 1 L4 1.2 L4.6 3.2 L3.6 4 Q4.4 5.8 6 6.4 L6.8 5.4 L8.8 6 L9 7.8 Q8 9 6.8 8.8 Q2.4 7.8 1.2 3.2 Q1 2 2.2 1 Z"/></svg></span>555-210-4400 ext. 22</li>
      <li><span class="icon-dot"><svg viewBox="0 0 10 10"><rect x="1" y="3" width="8" height="5" rx="1"/><rect x="3" y="1.5" width="4" height="2"/></svg></span>555-210-4471</li>
      <li><span class="icon-dot"><svg viewBox="0 0 10 10"><rect x="3" y="1" width="4" height="8" rx="0.8"/></svg></span>555-318-2260</li>
    </ul>
  </div>
  <div class="front-footer-base"></div>
</section>

</body>
</html>
```